New Branding Logo and Stationery Design Project

We are looking for a Stationary design for a company called "Peak Renewal". We are a Personal Training business that helps people of diverse ages, fitness levels and goals achieve what they aspire to. We are excellent at what we do and have a high rate of results. We are highly compassionate and love helping people. We want this to show in our logo. The logo must be able to be used on websites but also allow for large printing in the future also.

On the Business Card
Front we need the logo, and underneath this the words "Your health and fitness specialists".
On the back of the card we need:
Name (this will be different on the 2 peoples cards)
Health and fitness specialist
mobile: 04XX-XXX-XXX (we will give to the winner to add)
website: www.peakrenewal-example.com.au
email: info@peakrenewal-example.com.au
Down the bottom of the card we need a section that says something like:
"Your next appointment date is / / time : "

On the letterhead we will need:
Logo
Peak Renewal Pty Ltd
Address
Phone number
Email
Website

Target Market(s)

Anyone, any age who needs help with health and fitness

Industry/Entity Type

Printing

Requirements
Must have
• Templates for business cards here:
https://www.inkmarlow-example.com.au/businesscards_diy.php
Should not have
• Should not be Racist, Sexist, Ageist

```html
<!DOCTYPE html>
<html lang="en">
<head>
<meta charset="utf-8">
<title>Peak Renewal – Stationery</title>
<link rel="stylesheet" href="https://fonts.googleapis.com/css2?family=Ubuntu:wght@400;500&family=Nunito+Sans:wght@400&display=swap">
<style>
  :root {
    --brand-blue: #1f5cff;
    --ink: #1b1b1b;
    --paper: #ffffff;
    --field: #e4e4e4;
    --muted: #cfcfcf;
    --edge: #9a9a9a;
  }
  * { margin: 0; padding: 0; box-sizing: border-box; }
  html, body { width: 1200px; height: 960px; overflow: hidden; background: var(--paper); }
  body { position: relative; font-family: "Ubuntu", sans-serif; color: var(--ink); }

  .sheet { position: absolute; background: var(--paper); overflow: hidden; }
  .sheet svg.swoosh { position: absolute; left: 0; top: 0; width: 100%; height: 100%; }

  .letterhead { left: 170px; top: 123px; width: 510px; height: 661px; border: 1px solid var(--edge); }
  .card-front { left: 695px; top: 123px; width: 334px; height: 218px; border: 1px solid var(--edge); }
  .card-back  { left: 696px; top: 392px; width: 333px; height: 217px; background: var(--ink); }

  .brand { position: absolute; display: flex; flex-direction: column; }
  .brand-row { display: flex; align-items: center; }
  .brand-dot { border-radius: 50%; background: var(--brand-blue); flex: none; }
  .brand-name { color: var(--brand-blue); font-weight: 500; line-height: 1; white-space: nowrap; }
  .brand-tagline { color: var(--ink); font-weight: 400; white-space: nowrap; }

  .letterhead .brand { left: 270px; top: 40px; }
  .letterhead .brand-dot { width: 14px; height: 14px; margin-right: 8px; }
  .letterhead .brand-name { font-size: 24px; }
  .letterhead .brand-tagline { font-size: 9.5px; letter-spacing: 1.3px; margin: 5px 0 0 22px; }

  .letterhead .company-details {
    position: absolute; left: 32px; top: 573px;
    font-family: "Nunito Sans", sans-serif; font-size: 9px; line-height: 11px; list-style: none;
  }
  .letterhead .company-details li:first-child { margin-bottom: 3px; }

  .card-front .brand { left: 29px; top: 50px; }
  .card-front .brand-dot { width: 16px; height: 16px; margin-right: 9px; }
  .card-front .brand-name { font-size: 28px; }
  .card-front .brand-tagline { font-size: 10px; letter-spacing: 1.3px; margin: 6px 0 0 25px; }

  .card-back .emblem {
    position: absolute; left: 42px; top: 48px; width: 112px; height: 112px;
    border-radius: 50%; background: var(--brand-blue);
  }
  .card-back .contact {
    position: absolute; left: 167px; top: 54px; color: var(--paper);
    font-family: "Nunito Sans", sans-serif;
  }
  .contact .person-name { font-size: 10px; }
  .contact .person-role { font-size: 7px; color: var(--muted); margin-top: 4px; }
  .contact .lines { list-style: none; margin-top: 14px; font-size: 6.8px; line-height: 9px; color: var(--muted); }
  .contact .lines span { display: inline-block; width: 15px; }
  .contact .appointment { margin-top: 10px; font-size: 6.8px; color: var(--muted); }
  .contact .appointment-fields { display: flex; align-items: center; margin-top: 5px; font-size: 6.8px; color: var(--muted); }
  .appointment-fields .field { height: 15px; background: var(--field); border-radius: 2px; }
  .appointment-fields .date { width: 42px; }
  .appointment-fields .time { width: 36px; }
  .appointment-fields .sep { margin: 0 7px; }

  .brand-showcase { left: 695px; top: 662px; }
  .brand-showcase .brand-dot { width: 26px; height: 26px; margin-right: 14px; }
  .brand-showcase .brand-name { font-size: 46px; }
  .brand-showcase .brand-tagline { font-size: 15px; letter-spacing: 2px; margin: 9px 0 0 40px; }
</style>
</head>
<body>

  <section class="sheet letterhead" aria-label="Letterhead">
    <svg class="swoosh" viewBox="0 0 637 826" preserveAspectRatio="none" aria-hidden="true">
      <path d="M0 0 H365 C200 20 70 110 0 216 Z" fill="var(--ink)"/>
      <path d="M0 216 C50 130 120 70 185 32 C110 70 40 125 0 188 Z" fill="var(--brand-blue)"/>
      <path d="M637 600 C565 735 455 805 335 826 H637 Z" fill="var(--ink)"/>
      <path d="M637 600 C600 690 520 760 430 798 C535 770 605 700 637 630 Z" fill="var(--brand-blue)"/>
    </svg>
    <div class="brand">
      <div class="brand-row"><span class="brand-dot"></span><span class="brand-name">Peak Renewal</span></div>
      <span class="brand-tagline">Your Health &amp; Fitness Experts</span>
    </div>
    <ul class="company-details">
      <li>Peak Renewal Pty Ltd</li>
      <li>123 Smith Road, XXXXXX AU</li>
      <li>04XX-XXX-XXX</li>
      <li>info@peakrenewal-example.com.au</li>
      <li>www.peakrenewal-example.com.au</li>
    </ul>
  </section>

  <section class="sheet card-front" aria-label="Business card front">
    <svg class="swoosh" viewBox="0 0 417 272" preserveAspectRatio="none" aria-hidden="true">
      <path d="M417 80 C330 170 250 220 125 250 L0 230 V272 H417 Z" fill="var(--ink)"/>
      <path d="M417 42 V80 C330 170 250 220 170 240 C265 205 350 140 417 42 Z" fill="var(--brand-blue)"/>
      <path d="M0 203 C90 240 170 262 275 272 H235 C160 262 80 248 0 232 Z" fill="var(--brand-blue)"/>
    </svg>
    <div class="brand">
      <div class="brand-row"><span class="brand-dot"></span><span class="brand-name">Peak Renewal</span></div>
      <span class="brand-tagline">Your Health &amp; Fitness Experts</span>
    </div>
  </section>

  <section class="sheet card-back" aria-label="Business card back">
    <span class="emblem" aria-hidden="true"></span>
    <div class="contact">
      <p class="person-name">Mara</p>
      <p class="person-role">Health and Fitness Specialist</p>
      <ul class="lines">
        <li><span>PH</span>04XX XXX XXX</li>
        <li><span>WE</span>www.peakrenewal-example.com.au</li>
        <li><span>EM</span>info@peakrenewal-example.com.au</li>
      </ul>
      <p class="appointment">Your next appointment is on</p>
      <div class="appointment-fields">
        <span class="field date"></span><span class="sep">at</span><span class="field time"></span>
      </div>
    </div>
  </section>

  <div class="brand brand-showcase" aria-label="Brand name">
    <div class="brand-row"><span class="brand-dot"></span><span class="brand-name">Peak Renewal</span></div>
    <span class="brand-tagline">Your Health &amp; Fitness Experts</span>
  </div>

</body>
</html>
```